依頼詳細
国家資格に対応するための新規講習の開講を予定しまして新しいチラシを作成したいと思っております。
令和5年5月リリース予定の新規講習に関しましての広告及び講習に関する説明を行えるチラシのデザインをお願いいたします。
令和5年5月リリース予定ですが、既存の講習受講後に新規講習を追加で受ける形の受講も可能であるため、それまでの間の従来の講習も広告も行っていきたいと思っております。
従来の講習→新規講習の受講の流れを勧めたいです。

利用用途は新聞折込及び、ポスティングにて利用いたします。
希望はA4片面カラーを希望いたします。

納品はpsdファイルおよびPDFファイル(プリモアにすぐに入稿できる仕様)を希望いたします。
記載項目
■校名
ドローン教習所 翠光小樽校・道央MTR校
■空撮技能認定ロゴ

```html
<!DOCTYPE html>
<html lang="ja">
<head>
<meta charset="utf-8">
<title>国家試験コース開講 チラシ</title>
<link href="https://fonts.googleapis.com/css2?family=Noto+Sans+JP:wght@400;500;700;900&display=swap" rel="stylesheet">
<style>
:root{
  --navy:#0c2440;
  --navy-deep:#071829;
  --yellow:#ffe600;
  --yellow-soft:#fff27a;
  --green:#2f8f3a;
  --green-dark:#1d5a26;
  --forest-1:#3c5a32;
  --forest-2:#1f3a22;
  --ink:#1a1a1a;
  --white:#ffffff;
  --grey:#5a5a5a;
}
*{margin:0;padding:0;box-sizing:border-box}
html,body{width:846px;height:1200px;overflow:hidden;background:#fff}
body{font-family:"Noto Sans JP",sans-serif;color:var(--ink);position:relative}
.flyer{position:relative;width:846px;height:1200px;overflow:hidden;background:var(--navy)}

/* hero */
.hero{position:absolute;left:0;top:0;width:846px;height:340px;background:linear-gradient(180deg,var(--navy-deep),var(--navy) 70%,#15324f)}
.hero-photo{position:absolute;right:0;top:0;width:420px;height:330px;background:radial-gradient(ellipse at 60% 40%,#f2f4f6 0%,#c9d2da 40%,rgba(21,50,79,0) 75%)}
.school-tag{position:absolute;left:24px;top:14px;display:flex;align-items:center;gap:8px;background:var(--white);color:var(--navy);font-weight:700;font-size:17px;padding:3px 12px 3px 6px}
.school-tag .mark{width:18px;height:18px;background:var(--navy)}
.title{position:absolute;left:22px;top:40px;font-size:66px;font-weight:900;color:var(--yellow);letter-spacing:1px;line-height:1.1}
.about{position:absolute;left:26px;top:140px;width:440px;color:var(--white)}
.about h2{font-size:20px;font-weight:700;margin-bottom:8px}
.about p{font-size:11.5px;line-height:1.75}
.about .hl{color:var(--yellow);font-weight:700}
.start{position:absolute;left:26px;top:272px;display:flex;align-items:center;gap:10px;color:var(--white);font-weight:900}
.start .lead{font-size:32px}
.start .key{background:var(--yellow);color:var(--ink);font-size:34px;padding:2px 14px}
.start .tail{font-size:32px}

/* flow */
.flow{position:absolute;left:0;top:340px;width:846px;height:640px;background:linear-gradient(180deg,#2c4a2a,var(--forest-1) 40%,var(--forest-2))}
.flow-photo{position:absolute;inset:0;background:radial-gradient(ellipse at 70% 30%,rgba(120,150,90,.35),rgba(0,0,0,0) 60%)}
.flow svg.lines{position:absolute;left:0;top:0}
.step{position:absolute;left:26px;width:170px;border:2px solid var(--white);background:rgba(20,60,30,.75);color:var(--white);font-weight:700;font-size:17px;text-align:center;padding:10px 0}
.step.main{background:var(--green)}
.badge{position:absolute;display:flex;align-items:stretch;font-weight:900}
.badge .cap{background:var(--yellow);color:var(--ink);font-size:11px;text-align:center;padding:2px 4px}
.row{position:absolute;display:flex;align-items:center;gap:8px}
.pill{background:var(--yellow);color:var(--ink);font-weight:900;display:flex;align-items:center;gap:6px;padding:4px 12px;font-size:15px}
.pill .num{background:var(--ink);color:var(--yellow);font-size:22px;padding:0 6px}
.pill.white{background:var(--white)}
.small-cap{font-size:10px;color:var(--yellow);font-weight:700;text-align:center}
.exempt{background:var(--white);color:var(--ink);font-weight:900;display:flex;align-items:baseline;gap:4px;padding:4px 12px;font-size:15px}
.exempt .num{font-size:28px;color:#c8141e}
.big-exempt{position:absolute;left:575px;top:250px;width:110px;height:110px;border-radius:50%;background:var(--yellow);color:var(--ink);font-weight:900;text-align:center;display:flex;flex-direction:column;justify-content:center;line-height:1.1}
.big-exempt .num{font-size:40px;color:#c8141e}
.big-exempt .lbl{font-size:20px}
.note-tag{position:absolute;left:235px;top:147px;border:1px solid var(--white);color:var(--white);font-size:12px;padding:3px 10px}
.side{position:absolute;left:712px;width:112px;border:2px solid var(--white);color:var(--white);text-align:center;font-size:11px;padding:6px 4px;background:rgba(12,36,64,.75);line-height:1.5}
.side strong{display:block;font-size:15px}
.final{position:absolute;left:235px;top:437px;width:590px;background:var(--navy);color:var(--white);font-weight:700;font-size:18px;padding:10px 16px;border-left:6px solid var(--yellow)}
.final b{color:var(--yellow)}
.footnote{position:absolute;left:0;top:590px;width:846px;text-align:center;color:var(--white);font-size:12px;background:rgba(0,0,0,.35);padding:8px 0}

/* info */
.info{position:absolute;left:0;top:980px;width:846px;height:130px;background:var(--white);display:flex;gap:24px;padding:14px 26px}
.info section{flex:1}
.info h3{display:inline-block;background:var(--green);color:var(--white);font-size:12px;font-weight:700;padding:2px 10px;margin-bottom:6px}
.info p{font-size:10.5px;line-height:1.65;color:var(--grey)}

/* footer */
.footer{position:absolute;left:0;top:1110px;width:846px;height:90px;background:var(--white);border-top:3px solid var(--green);display:flex;align-items:center;padding:0 26px;gap:20px}
.brand{display:flex;align-items:center;gap:10px;font-size:30px;font-weight:900;color:var(--green-dark)}
.brand .dot{width:26px;height:26px;border-radius:50%;background:var(--green-dark)}
.contact{margin-left:auto;text-align:right}
.contact .name{font-size:14px;font-weight:700;color:var(--ink)}
.contact .tel{font-size:34px;font-weight:900;color:var(--green-dark);display:flex;align-items:center;gap:8px;justify-content:flex-end;line-height:1.1}
.contact .web{font-size:10px;color:var(--grey)}
</style>
</head>
<body>
<div class="flyer">

  <header class="hero">
    <div class="hero-photo" role="img" aria-label="空に浮かぶ白いドローンの写真"></div>
    <div class="school-tag"><span class="mark"></span>ドローン教習所</div>
    <h1 class="title">国家試験コース開講!</h1>
    <div class="about">
      <h2>国家試験とは</h2>
      <p>登録講習機関を受講した上で国家試験を受験すると、無人航空機操縦者技能証明（ドローン国家ライセンス）を取得できます。当校の講習を修了することで国家試験の<span class="hl">「実地試験免除」</span>となり、指定試験機関では<span class="hl">「学科試験」</span>が受験可能です。</p>
    </div>
    <div class="start">
      <span class="lead">まずは</span><span class="key">基礎技能講習</span><span class="tail">から始めよう!</span>
    </div>
  </header>

  <main class="flow">
    <div class="flow-photo" role="img" aria-label="上空から見た森と丘の風景写真"></div>
    <svg class="lines" width="846" height="640" viewBox="0 0 846 640" aria-hidden="true">
      <g stroke="#ffffff" stroke-width="3" fill="#ffffff">
        <line x1="111" y1="75" x2="111" y2="135"/><polygon points="103,130 119,130 111,142"/>
        <line x1="111" y1="180" x2="111" y2="235"/><polygon points="103,230 119,230 111,242"/>
        <line x1="111" y1="375" x2="111" y2="425"/><polygon points="103,420 119,420 111,432"/>
        <line x1="196" y1="55" x2="228" y2="55"/>
        <line x1="196" y1="160" x2="228" y2="160"/>
        <line x1="196" y1="305" x2="228" y2="305"/>
      </g>
      <g fill="#ffe600">
        <polygon points="420,45 434,55 420,65"/>
        <polygon points="420,270 434,280 420,290"/>
        <polygon points="420,335 434,345 420,355"/>
      </g>
    </svg>

    <div class="step" style="top:32px">基礎技能講習</div>
    <div class="row" style="left:235px;top:32px">
      <div><div class="small-cap">空撮技能認定</div><div class="pill"><span class="num">3</span>・<span class="num">4</span>級 所有</div></div>
    </div>
    <div class="row" style="left:445px;top:30px">
      <div><div class="small-cap">学科試験</div><div class="exempt"><span class="num">4</span>時間 免除</div></div>
    </div>

    <div class="step" style="top:142px">実機飛行実績</div>
    <div class="note-tag">3時間以上の実機飛行実績</div>

    <div class="step main" style="top:245px;padding:50px 0">国家試験コース</div>
    <div class="row" style="left:235px;top:257px">
      <div><div class="small-cap">空撮技能認定</div><div class="pill"><span class="num">1</span>・<span class="num">2</span>級 所有</div></div>
    </div>
    <div class="row" style="left:445px;top:257px">
      <div><div class="small-cap">学科試験</div><div class="exempt"><span class="num">7</span>時間 免除</div></div>
    </div>
    <div class="row" style="left:235px;top:322px">
      <div class="pill"><span class="num">3</span>・<span class="num">4</span>級 所有</div>
    </div>
    <div class="row" style="left:445px;top:320px">
      <div class="exempt"><span class="num">6</span>時間 免除</div>
    </div>
    <div class="big-exempt"><span class="num">8</span><span class="lbl">時間<br>免除</span></div>

    <div class="side" style="top:30px"><strong>ドローン<br>経験者</strong>学科・実地<br>短縮コース</div>
    <div class="side" style="top:240px"><strong>初学者</strong>学科＋11時間<br>実地＋10時間</div>

    <div class="step" style="top:437px">指定試験機関</div>
    <div class="final"><b>指定試験機関</b>にて学科試験及び、身体検査</div>

    <p class="footnote">経験者受講時には弊社実機で合計3時間以上の飛行実績が必要です。</p>
  </main>

  <div class="info">
    <section>
      <h3>国家試験コース内容</h3>
      <p>学科講習・実地講習を行い、実地試験までを一貫して実施します。空撮技能認定をお持ちの方は学科の一部が免除となり、短期間で国家試験の受験が可能です。受講の詳細は各校までお問い合わせください。</p>
    </section>
    <section>
      <h3>講習スケジュール</h3>
      <p>受講者様のご希望に合わせて日程を調整いたします。平日・土日ともに受講可能です。令和5年5月より国家試験コースを開講予定、それまでは従来の講習も受付中です。</p>
    </section>
  </div>

  <footer class="footer">
    <div class="brand"><span class="dot"></span>空撮技能認定</div>
    <div class="contact">
      <div class="name">ドローン教習所 翠光小樽校・道央MTR校</div>
      <div class="tel">
        <svg width="28" height="28" viewBox="0 0 24 24" aria-hidden="true"><path fill="#1d5a26" d="M6.6 10.8a15.1 15.1 0 0 0 6.6 6.6l2.2-2.2a1 1 0 0 1 1-.25 11.4 11.4 0 0 0 3.6.57 1 1 0 0 1 1 1V20a1 1 0 0 1-1 1A17 17 0 0 1 3 4a1 1 0 0 1 1-1h3.5a1 1 0 0 1 1 1c0 1.25.2 2.45.57 3.57a1 1 0 0 1-.25 1z"/></svg>
        0134-00-5821
      </div>
      <div class="web">info@kuusatsu-gino.jp ／ www.kuusatsu-gino.jp</div>
    </div>
  </footer>

</div>
</body>
</html>
```